Iron Harbor Preparedness & Outfitters
Business Cards & Stationery
Cutting-Edge
Dale Whitmore
Owner/ Director of Development
4173 Quarry Ln.
Sacramento, CA 95867
1-855-ironharbor
dw@ironharborgear-example.com
www.ironharborgear-example.com
Iron Harbor logo eps
iron harbor ai
Vector
winning_logo

```html
<!DOCTYPE html>
<html lang="en">
<head>
<meta charset="utf-8">
<title>Iron Harbor Preparedness &amp; Outfitters — Stationery</title>
<link rel="stylesheet" href="https://fonts.googleapis.com/css2?family=Oswald:wght@700&family=Open+Sans:wght@400;600&display=swap">
<style>
  :root {
    --backdrop: #e8e5e0;
    --paper: #ffffff;
    --brand-yellow: #f3e00c;
    --brand-black: #141414;
    --ink: #2b2b2b;
    --muted: #6d6d6d;
    --shadow: rgba(0,0,0,.22);
  }
  * { margin: 0; padding: 0; box-sizing: border-box; }
  html, body { width: 1200px; height: 456px; overflow: hidden; }
  body {
    position: relative;
    background: var(--backdrop);
    font-family: "Open Sans", Arial, sans-serif;
    color: var(--ink);
  }
  .piece { position: absolute; box-shadow: 0 2px 6px var(--shadow); overflow: hidden; background: var(--paper); }
  .piece svg.art { position: absolute; inset: 0; }
  .wordmark {
    font-family: "Oswald", Impact, sans-serif;
    font-weight: 700;
    color: var(--brand-black);
    text-transform: uppercase;
    line-height: 1;
    display: flex;
    align-items: center;
    gap: 4px;
    white-space: nowrap;
  }
  .wordmark .dot { display: inline-block; border-radius: 50%; background: var(--brand-black); flex: none; }
  .caption {
    position: absolute;
    font-size: 7px;
    color: var(--muted);
    text-align: center;
  }

  /* Brand intro */
  .brand-intro { position: absolute; left: 22px; top: 96px; width: 120px; }
  .brand-intro .wordmark { font-size: 22px; flex-direction: column; align-items: flex-start; gap: 2px; }
  .brand-intro .tagline { margin-top: 8px; font-size: 9px; color: var(--muted); }

  /* Business cards */
  .business-card { left: 24px; width: 114px; height: 66px; }
  .card-front { top: 238px; }
  .card-back { top: 356px; }
  .business-card .wordmark { position: absolute; left: 7px; top: 8px; font-size: 8.5px; gap: 3px; }
  .business-card .wordmark .dot { width: 6px; height: 6px; }
  .card-contact {
    position: absolute; right: 5px; top: 8px;
    font-size: 3.4px; line-height: 4.8px; color: var(--ink); text-align: right;
  }
  .card-person { position: absolute; left: 8px; top: 36px; font-size: 4.4px; line-height: 5.6px; color: var(--paper); }
  .card-person strong { color: var(--brand-yellow); font-weight: 600; }
  .card-web { position: absolute; left: 8px; bottom: 6px; font-size: 4px; color: var(--paper); }

  /* Letterheads */
  .letterhead { top: 30px; width: 310px; height: 408px; }
  .letterhead-one { left: 190px; }
  .letterhead-two { left: 532px; }
  .letterhead .wordmark { position: absolute; }
  .letterhead-one .wordmark { left: 62px; top: 13px; font-size: 15px; }
  .letterhead-one .wordmark .dot { width: 9px; height: 9px; }
  .letterhead-two .wordmark { left: 104px; top: 14px; font-size: 17px; }
  .letterhead-two .wordmark .dot { width: 10px; height: 10px; }
  .letterhead-contact {
    position: absolute; left: 190px; top: 9px;
    font-size: 4.2px; line-height: 5.6px; color: var(--ink);
  }
  .letterhead-footer {
    position: absolute; left: 0; right: 0; bottom: 10px;
    font-size: 4.2px; line-height: 5.6px; text-align: center; color: var(--muted);
  }

  /* Envelope */
  .envelope { left: 862px; top: 104px; width: 314px; height: 168px; }
  .envelope .wordmark { position: absolute; left: 122px; top: 20px; font-size: 15px; }
  .envelope .wordmark .dot { width: 9px; height: 9px; }

  /* Compliments slip */
  .compliment-slip { left: 862px; top: 344px; width: 314px; height: 96px; }
  .compliment-slip .wordmark { position: absolute; left: 12px; top: 9px; font-size: 13px; }
  .compliment-slip .wordmark .dot { width: 8px; height: 8px; }
  .slip-note { position: absolute; left: 120px; top: 26px; font-size: 5px; color: var(--muted); }
</style>
</head>
<body>

  <section class="brand-intro">
    <div class="wordmark"><span>Iron</span><span>Harbor</span></div>
    <p class="tagline">Stationery Concepts</p>
  </section>

  <article class="piece business-card card-front">
    <svg class="art" width="114" height="66" viewBox="0 0 114 66">
      <path d="M0 30 C30 22 70 22 114 28 L114 66 L0 66 Z" fill="var(--brand-yellow)"/>
      <path d="M0 34 C32 26 72 27 114 33 L114 66 L0 66 Z" fill="var(--brand-black)"/>
    </svg>
    <div class="wordmark"><span class="dot"></span><span>Iron Harbor</span></div>
    <div class="card-contact">1-855-ironharbor<br>4173 Quarry Ln.<br>Sacramento, CA 95867</div>
    <div class="card-person"><strong>Dale Whitmore</strong><br>Owner/ Director of Development</div>
    <div class="card-web">dw@ironharborgear-example.com</div>
  </article>
  <p class="caption" style="left:24px; top:307px; width:114px;">Business Card Front</p>

  <article class="piece business-card card-back">
    <svg class="art" width="114" height="66" viewBox="0 0 114 66">
      <path d="M0 30 C30 22 70 22 114 28 L114 66 L0 66 Z" fill="var(--brand-yellow)"/>
      <path d="M0 34 C32 26 72 27 114 33 L114 66 L0 66 Z" fill="var(--brand-black)"/>
    </svg>
    <div class="wordmark"><span class="dot"></span><span>Iron Harbor</span></div>
    <div class="card-person"><strong>Preparedness &amp; Outfitters</strong><br>www.ironharborgear-example.com</div>
  </article>
  <p class="caption" style="left:24px; top:425px; width:114px;">Business Card Back</p>

  <article class="piece letterhead letterhead-one">
    <svg class="art" width="310" height="408" viewBox="0 0 310 408">
      <path d="M0 0 H310 V40 C220 34 90 38 0 50 Z" fill="var(--brand-yellow)"/>
      <path d="M0 50 C90 38 220 34 310 40 L310 44 C220 39 90 44 0 58 Z" fill="var(--brand-black)"/>
      <line x1="20" y1="392" x2="290" y2="392" stroke="var(--brand-yellow)" stroke-width="1"/>
    </svg>
    <div class="wordmark"><span class="dot"></span><span>Iron Harbor</span></div>
    <div class="letterhead-contact">1-855-ironharbor<br>4173 Quarry Ln.<br>Sacramento, CA 95867<br>www.ironharborgear-example.com</div>
    <div class="letterhead-footer">dw@ironharborgear-example.com</div>
  </article>
  <p class="caption" style="left:190px; top:442px; width:310px;">Letterhead Style 01</p>

  <article class="piece letterhead letterhead-two">
    <svg class="art" width="308" height="408" viewBox="0 0 308 408">
      <path d="M0 50 C80 40 200 36 308 42 L308 48 C200 43 80 47 0 58 Z" fill="var(--brand-black)"/>
      <path d="M0 58 C80 47 200 43 308 48 L308 52 C200 48 80 52 0 62 Z" fill="var(--brand-yellow)"/>
    </svg>
    <div class="wordmark"><span class="dot"></span><span>Iron Harbor</span></div>
    <div class="letterhead-footer">4173 Quarry Ln. Sacramento, CA 95867 · 1-855-ironharbor<br>dw@ironharborgear-example.com · www.ironharborgear-example.com</div>
  </article>
  <p class="caption" style="left:532px; top:442px; width:308px;">Letterhead Style 02</p>

  <article class="piece envelope">
    <svg class="art" width="314" height="168" viewBox="0 0 314 168">
      <path d="M0 0 H314 L157 74 Z" fill="var(--brand-yellow)"/>
      <path d="M0 0 L157 74 L314 0" fill="none" stroke="var(--brand-black)" stroke-width="1.5"/>
      <path d="M0 168 L132 74 M314 168 L182 74" stroke="#d8d8d8" stroke-width="1" fill="none"/>
    </svg>
    <div class="wordmark"><span class="dot"></span><span>Iron Harbor</span></div>
  </article>
  <p class="caption" style="left:862px; top:278px; width:314px;">Envelope Design</p>

  <article class="piece compliment-slip">
    <svg class="art" width="314" height="96" viewBox="0 0 314 96">
      <path d="M0 0 H314 V6 C200 8 80 18 0 36 Z" fill="var(--brand-yellow)"/>
      <path d="M0 36 C80 18 200 8 314 6 L314 10 C200 13 80 23 0 41 Z" fill="var(--brand-black)"/>
    </svg>
    <div class="wordmark"><span class="dot"></span><span>Iron Harbor</span></div>
    <p class="slip-note">With Compliments</p>
  </article>
  <p class="caption" style="left:862px; top:444px; width:314px;">Compliment Slip</p>

</body>
</html>
```